New business card for UK roofing company

We are Brindmore Roofing and we need a business card design for our staff.

We offer the following services:

- New roofs
- General roof repairs
- Drone surveys
- Single ply roofing
- Steel cladding
- Asbestos removal
- Electronic leak detection

I have attached our logo. I have also attached example branding printed to our vans. The business card should fit in with the style of our branding.

The business card should have the following information;

Address:
Unit 17c Wendlecroft Farm
Wendlecroft Lane
Hatchington
CM4 9QD

Telephone: 020 7946 0372
24 Hour: 0800 612 4479

Email: ray@brindmoreroofing.example
Mobile: 07700981234
Name: Ray Tunstead
Website: www.brindmoreroofing.example

The business card will be printed in Spot UV, see here: https://www.kestaprint.example/business-cards/spot-uv/

If you need anymore info, please let me know,

```html
<!DOCTYPE html>
<html lang="en">
<head>
<meta charset="utf-8">
<title>Brindmore Roofing – Business Card</title>
<link rel="stylesheet" href="https://fonts.googleapis.com/css2?family=Poppins:wght@300;400;500;700;800&display=swap">
<style>
  :root {
    --navy: #114a7a;
    --cyan: #00aedb;
    --ink: #1b1b1b;
    --card: #ffffff;
    --backdrop: #f1f1f1;
  }
  * { box-sizing: border-box; margin: 0; padding: 0; }
  html, body {
    width: 878px; height: 1200px; overflow: hidden;
    background: var(--backdrop);
    font-family: "Poppins", sans-serif;
    color: var(--ink);
  }
  .card {
    position: absolute; left: 183px;
    width: 512px; height: 331px;
    background: var(--card);
    overflow: hidden;
  }
  .card--front { top: 205px; }
  .card--back  { top: 640px; }
  .card__bands { position: absolute; inset: 0; width: 100%; height: 100%; }

  .brand {
    position: absolute;
    display: flex; align-items: center;
    color: var(--navy); font-weight: 700; letter-spacing: -0.5px;
    white-space: nowrap;
  }
  .brand__dot { border-radius: 50%; background: var(--cyan); flex: none; }
  .card--front .brand { left: 0; right: 0; top: 142px; justify-content: center; gap: 10px; font-size: 34px; }
  .card--front .brand__dot { width: 34px; height: 34px; }
  .card--back .brand { right: 20px; top: 30px; gap: 6px; font-size: 20px; }
  .card--back .brand__dot { width: 20px; height: 20px; }

  .services { position: absolute; left: 0; right: 0; top: 238px; text-align: center; }
  .services__title { font-size: 9px; font-weight: 700; letter-spacing: 2.6px; text-transform: uppercase; margin-bottom: 4px; }
  .services__list { font-size: 12.5px; font-weight: 300; line-height: 15.5px; }

  .person { position: absolute; left: 28px; top: 136px; font-size: 25px; color: var(--navy); text-transform: uppercase; }
  .person__first { font-weight: 300; }
  .person__last { font-weight: 800; }

  .contact { position: absolute; left: 28px; top: 176px; font-size: 12.5px; font-weight: 300; line-height: 20.5px; white-space: nowrap; }
  .contact b, .address b, .hotlines b { font-weight: 500; }
  .address { position: absolute; left: 300px; top: 177px; font-size: 12.5px; font-weight: 300; line-height: 16.5px; white-space: nowrap; }

  .hotlines { position: absolute; left: 28px; right: 0; top: 294px; display: flex; color: #fff; font-size: 13.5px; font-weight: 300; white-space: nowrap; }
  .hotlines span:first-child { width: 231px; }
</style>
</head>
<body>

<section class="card card--front">
  <svg class="card__bands" viewBox="0 0 963 622" preserveAspectRatio="none" aria-hidden="true">
    <polygon points="0,0 963,0 963,155 0,47" fill="var(--navy)"/>
    <polygon points="0,47 700,125.5 0,61" fill="var(--cyan)"/>
  </svg>
  <div class="brand"><span class="brand__dot"></span>Brindmore Roofing</div>
  <div class="services">
    <p class="services__title">We offer the following services:</p>
    <p class="services__list">New Roofs, General Roof Repairs, Drone Surveys<br>Single Ply Roofing, Steel Cladding, Asbestos Removal<br>Electronic Leak Detection</p>
  </div>
</section>

<section class="card card--back">
  <svg class="card__bands" viewBox="0 0 963 622" preserveAspectRatio="none" aria-hidden="true">
    <polygon points="0,530 963,497 963,500 0,541" fill="var(--cyan)"/>
    <polygon points="0,541 963,500 963,622 0,622" fill="var(--navy)"/>
  </svg>
  <div class="brand"><span class="brand__dot"></span>Brindmore Roofing</div>
  <h1 class="person"><span class="person__first">Ray</span> <span class="person__last">Tunstead</span></h1>
  <div class="contact">
    <p><b>Email:</b> ray@brindmoreroofing.example</p>
    <p><b>Mobile:</b> 0770 0981 234</p>
    <p><b>Website:</b> www.brindmoreroofing.example</p>
  </div>
  <address class="address" style="font-style:normal">
    <b>Address:</b><br>Unit 17c Wendlecroft Farm<br>Wendlecroft Lane<br>Hatchington CM4 9QD
  </address>
  <div class="hotlines">
    <span><b>Telephone:</b> 020 7946 0372</span>
    <span><b>24 Hour:</b> 0800 612 4479</span>
  </div>
</section>

</body>
</html>
```